依頼詳細
【サイトマップ】
TOPページ
---HOME
---COMPANY (会社概要/会社沿革)
---BUSINESS (事業内容)
---RECRUIT  (採用情報)
---CONTACT  (問い合わせ)
---NEWS  (新着情報)
【サイト作成においてのポイント】
・レスポンシブデザインでお願いいたします。
・各所の素材は全てURLをお送り下さい。

【イメージ全体配置構図(いれていただきたい要素)】

ワイヤーフレームをご確認ください。
①~⑧までワイヤーフレーム内にふった番号順に詳細を記載しております。

※ワイヤーフレームはあくまでも入れたい要素を並べた一例になります。
各配置、表示位置は変えていただいても問題ございません。
------------------------

①グローバルナビ
配置は上部でお願いいたします。位置は中央を希望いたします。
------

②メインビジュアル
メインビジュアルは動画(アニメーション)挿入の仕様想定で作成して頂きたいです。
参考サイト:http://www.kelvora-sample.com/
http://updates.pimaru-breeze.jp/

1ページまるごと動画(アニメーション)仕様でも問題ございません。
参考サイト:http://www.tosquivel.com/

(こちらでは素材を用意しておりません。確認後、購入手続きをさせていただきますのでURLをお送りください)
サイズはどのデバイスでも横幅が100%になるように考えております。
縦幅はお任せしますので、素材にあわせていただけますと幸いです。
------

③新着情報
新着情報は3つ以上いれていただけますと幸いです
いれていただきたい要素は
・更新日時(年,月,日)
・更新内容のテキスト部分 20文字前後

各テキストの配置箇所、文字色、フォント、文字やボタンのサイズ、幅感等の指定はございません。
ワイヤーフレームにはいれていただきたい要素だけならべています。
------

④事業紹介箇所
入れていただきたい要素は以下になります。
・事業紹介イメージ素材
メイン動画がヘッダー部分のみに表示の場合
背景画像として、サイズは横が100%になるように考えております。
メイン動画が全体の場合
イメージ素材が浮き上がってくるようなアニメーション仕様で考えておりますので、その仕様にあったサイズ、表示方法にしていただけますと幸いです。

極力どのデバイスサイズでもバランスよく見えるような素材をご使用いただけますと幸いです。

・事業内容の名前
(Internet media、Promotion、Influencer Marketing)
・以下テキスト
(KanoMireaはインターネットを軸とした事業を展開しております。)
・下層ページへのリンクボタン

------

⑤入れていただきたい要素は以下になります。
・背景素材
メイン動画がヘッダー部分のみに表示の場合
メイン動画が全体の場合

・遷移先の中に含まれる内容の紹介
(Staff Interview、One Day、Blog)
・以下テキスト
(KanoMireaの福利厚生や、メンバーの1日の勤務スケジュールを公開)
・下層ページへのリンクボタン

------

⑥入れていただきたい要素は以下になります。
・背景素材
メイン動画がヘッダー部分のみに表示の場合
メイン動画が全体の場合

・遷移先の中に含まれる内容の紹介
(overview/ history、Greeting)
・以下テキスト
(会社概要・沿革・代表挨拶)
・下層ページへのリンクボタン

------

⑦フッター
サイト案内
------

⑧会社情報、ロゴ

以上になります。

ご不明点等がございましたらお気軽にお問い合わせ下さい。
何卒よろしくお願い申し上げます。
ページ数
1ページ
希望イメージ
• +5 0 +5
• シンプル
複雑
• 単色
カラフル
• 暗い
明るい
• 日常
高級
• 遊び心
厳粛
• 未来的
伝統的
• 女性的
男性的
希望する色
青系、水色系、グレー系、紫系
納品ファイル
• フォトショップ形式 (.psd)
補足説明
SD又は、FireworksPNGデータ
動画に関しましてはデータ添付またはURLをお送りいただけますと幸いです。
依頼公開後の追記内容
もう少し様々な作品を拝見させていただきたく、延長させていただきました。
引き続き、何卒よろしくお願いいたします。
■ 選んだ理由

全体の雰囲気が1番理想とするものに近く、構図も綺麗なバランスで組み立てられていました。
コーポレートサイトとしてシンプルかつおしゃれ見やすいものに仕上がると思い、rusofu様の作品を選ばせていただきました。

■ 提案者全員のお礼・コメント

各ランサー様
この度は弊社へのコンペへご参加いただき、誠にありがとうございました。
どの作品も大変素晴らしく、当選させていただきたいアイディア、デザインがたくさんありました。
また機会がございましたら、作品をご投稿下さいますと幸いに存じます。
誠にありがとうございました。

```html
<!DOCTYPE html>
<html lang="ja">
<head>
<meta charset="utf-8">
<title>Kano Mirea | コーポレートサイト</title>
<link rel="stylesheet" href="https://fonts.googleapis.com/css2?family=Noto+Sans+JP:wght@400;500;700&family=Montserrat:wght@300;400;600&family=Playfair+Display:ital@1&display=swap">
<style>
:root{
  --blue:#1e9fd6;
  --blue-deep:#1479b8;
  --blue-light:#5cc4ee;
  --ink:#333a40;
  --muted:#7b838a;
  --line:#d9dee2;
  --pale:#f3f5f7;
  --white:#ffffff;
}
*{margin:0;padding:0;box-sizing:border-box}
html,body{width:1200px;height:2664px;overflow:hidden;background:var(--white)}
body{font-family:"Noto Sans JP",sans-serif;color:var(--ink);position:relative}
.abs{position:absolute}

/* Global nav */
.global-nav{position:absolute;top:0;left:0;width:1200px;height:90px;display:flex;justify-content:center;gap:64px;align-items:center;z-index:2}
.global-nav a{font-family:"Montserrat",sans-serif;font-size:14px;letter-spacing:.08em;color:var(--ink);text-decoration:none}

/* Hero */
.hero{position:absolute;top:0;left:0;width:1200px;height:660px;background:linear-gradient(120deg,#ffffff 0%,#f4f6f8 55%,#e3e7ea 100%)}
.hero-visual{position:absolute;right:0;top:0;width:640px;height:660px;background:radial-gradient(ellipse at 70% 40%,#d5dadf 0%,rgba(230,233,236,.5) 45%,rgba(255,255,255,0) 75%)}
.hero-brand{position:absolute;left:250px;top:248px;display:flex;align-items:center;gap:22px}
.brand-dot{width:96px;height:96px;border-radius:50%;background:#3c4248}
.brand-name{font-family:"Montserrat",sans-serif;font-weight:600;font-size:42px;color:#3c4248;letter-spacing:.02em}
.hero-lead{position:absolute;left:250px;top:420px;font-size:15px;line-height:30px;color:var(--ink)}

/* News */
.news{position:absolute;top:660px;left:0;width:1200px;height:240px;background:linear-gradient(100deg,var(--blue-deep) 0%,var(--blue) 55%,var(--blue-light) 100%);color:var(--white)}
.news-label{position:absolute;left:70px;top:60px;display:flex;align-items:center;gap:14px;font-family:"Montserrat",sans-serif;font-size:18px;letter-spacing:.1em}
.news-list{position:absolute;left:220px;top:40px;display:flex;gap:60px}
.news-item{width:230px}
.news-date{font-family:"Playfair Display",serif;font-style:italic;font-size:26px;margin-bottom:12px}
.news-title{font-size:14px;font-weight:700;margin-bottom:8px}
.news-text{font-size:12px;line-height:22px;opacity:.92}

/* Business */
.business{position:absolute;top:912px;left:0;width:1200px;height:470px;background:linear-gradient(90deg,#8c9298 0%,#c9cdd1 35%,#e9ebed 65%,#dfe2e5 100%)}
.section-bar{position:absolute;left:0;top:20px;width:1200px;height:44px;background:rgba(255,255,255,.55);display:flex;align-items:center;padding-left:60px;gap:14px}
.section-bar .en{font-family:"Montserrat",sans-serif;font-size:15px;letter-spacing:.1em;color:var(--ink)}
.section-bar .ja{font-size:12px;color:var(--ink)}
.business-sign{position:absolute;left:150px;top:200px;display:flex;align-items:center;gap:18px}
.business-sign .brand-dot{width:90px;height:90px;background:rgba(255,255,255,.9)}
.business-sign .brand-name{font-size:58px;color:rgba(255,255,255,.92)}
.service-map{position:absolute;left:640px;top:70px;width:460px;height:330px}
.service{position:absolute;width:130px;height:130px;border-radius:50%;background:rgba(255,255,255,.92);border:3px solid var(--blue);display:flex;flex-direction:column;align-items:center;justify-content:center;text-align:center;font-family:"Montserrat",sans-serif;font-size:11px;line-height:15px;color:var(--ink);letter-spacing:.05em}
.service svg{margin-bottom:6px}
.btn-more{position:absolute;display:flex;align-items:center;justify-content:center;height:28px;width:150px;background:var(--blue-deep);color:var(--white);font-family:"Montserrat",sans-serif;font-size:11px;letter-spacing:.1em}

/* Recruit */
.recruit{position:absolute;top:1400px;left:0;width:1200px;height:340px;background:var(--white)}
.recruit-head{position:absolute;left:60px;top:16px;display:flex;gap:18px;align-items:center}
.recruit-head .en{font-family:"Montserrat",sans-serif;font-size:15px;letter-spacing:.1em}
.recruit-head .ja{font-size:12px}
.recruit-card{position:absolute;top:70px;width:270px}
.card-label{font-family:"Montserrat",sans-serif;font-size:13px;line-height:18px;letter-spacing:.06em;height:40px}
.card-photo{width:270px;height:215px;position:relative}
.card-tag{position:absolute;right:0;bottom:0;width:46px;height:46px;background:var(--blue)}

/* Company */
.company{position:absolute;top:1780px;left:0;width:1200px;height:500px;background:linear-gradient(180deg,#dfe3e7 0%,#eef0f2 100%)}
.company-head{position:absolute;left:60px;top:20px;display:flex;gap:14px;align-items:center}
.company-head .en{font-family:"Montserrat",sans-serif;font-size:15px;letter-spacing:.1em}
.greeting-title{position:absolute;left:220px;top:60px;font-family:"Montserrat",sans-serif;font-weight:300;font-size:70px;letter-spacing:.04em;color:#c3c8cd}
.greeting-name{position:absolute;left:225px;top:150px;font-size:13px;color:var(--blue-deep)}
.greeting-text{position:absolute;left:225px;top:180px;width:430px;font-size:12px;line-height:22px;color:var(--ink)}
.president-photo{position:absolute;left:800px;top:50px;width:360px;height:450px;background:linear-gradient(180deg,#e3e6e9 0%,#b7bcc2 60%,#4b5259 100%)}
.company-thumb{position:absolute;top:330px;width:200px;height:110px}
.thumb-label{position:absolute;right:10px;bottom:12px;text-align:right;font-family:"Montserrat",sans-serif;font-size:11px;line-height:14px;color:var(--white)}

/* Footer */
.site-footer{position:absolute;top:2280px;left:0;width:1200px;height:340px;background:var(--white)}
.footer-nav{position:absolute;left:220px;top:40px;display:flex;gap:0}
.footer-col{width:160px;text-align:center}
.footer-col h3{font-family:"Montserrat",sans-serif;font-weight:400;font-size:16px;letter-spacing:.08em;border-bottom:1px solid var(--line);padding-bottom:4px;margin:0 14px}
.footer-col .sub{font-size:10px;color:var(--muted);margin-top:4px}
.footer-col ul{list-style:none;margin-top:18px;text-align:left;padding-left:38px}
.footer-col li{font-size:11px;line-height:26px;color:var(--muted)}
.to-top{position:absolute;left:180px;top:230px;width:44px;height:44px;border-radius:6px;background:#e3eef6;display:flex;align-items:center;justify-content:center}
.footer-brand{position:absolute;left:890px;top:228px;display:flex;align-items:center;gap:10px}
.footer-brand .brand-dot{width:28px;height:28px;background:var(--blue)}
.footer-brand .brand-name{font-size:20px;color:var(--blue-deep)}
.footer-address{position:absolute;left:910px;top:265px;font-size:10px;line-height:16px;color:var(--muted);text-align:right;width:250px}
.copyright{position:absolute;top:2620px;left:0;width:1200px;height:44px;background:var(--blue-deep);color:var(--white);font-family:"Montserrat",sans-serif;font-size:10px;display:flex;align-items:center;justify-content:center;letter-spacing:.06em}
</style>
</head>
<body>

<section class="hero">
  <div class="hero-visual" role="img" aria-label="淡いグレーの幾何学ポリゴン背景(動画挿入エリア)"></div>
  <nav class="global-nav">
    <a href="#">HOME</a><a href="#">COMPANY</a><a href="#">BUSINESS</a><a href="#">RECRUIT</a><a href="#">CONTACT</a><a href="#">NEWS</a>
  </nav>
  <div class="hero-brand"><span class="brand-dot"></span><span class="brand-name">Kano Mirea</span></div>
  <p class="hero-lead">インターネットのホームページの広告、<br>制作及び運営管理インターネットを利用した各種情報提供サービス業</p>
</section>

<section class="news">
  <div class="news-label">
    <svg width="26" height="20" viewBox="0 0 26 20"><rect x="1" y="1" width="24" height="18" rx="2" fill="none" stroke="#fff" stroke-width="2"/><line x1="5" y1="7" x2="21" y2="7" stroke="#fff" stroke-width="2"/><line x1="5" y1="12" x2="17" y2="12" stroke="#fff" stroke-width="2"/></svg>
    NEWS
  </div>
  <div class="news-list">
    <article class="news-item">
      <p class="news-date">2017.4.3</p>
      <p class="news-title">【業務移転のお知らせ】</p>
      <p class="news-text">この度、4月3日より事務所を移転しました。新しい事務所にて、皆様のお越しをお待ちしております。</p>
    </article>
    <article class="news-item">
      <p class="news-date">2016.12.3</p>
      <p class="news-title">【年末年始休業のお知らせ】</p>
      <p class="news-text">今年も残りわずか、あらためてお知らせします。年末年始の期間は休業とさせていただきます。</p>
    </article>
    <article class="news-item">
      <p class="news-date">2016.11.18</p>
      <p class="news-title">【サイト公開のお知らせ】</p>
      <p class="news-text">コーポレートサイトを公開いたしました。今後ともどうぞよろしくお願いいたします。</p>
    </article>
  </div>
</section>

<section class="business">
  <div class="abs" role="img" aria-label="明るいオフィスエントランスの写真" style="inset:0;background:linear-gradient(90deg,rgba(120,126,132,.35),rgba(255,255,255,0) 60%)"></div>
  <div class="section-bar"><span class="en">BUSINESS</span><span class="ja">KanoMireaはインターネットを軸とした事業を展開しております。</span></div>
  <div class="business-sign"><span class="brand-dot"></span><span class="brand-name">Kano Mirea</span></div>
  <div class="service-map">
    <svg class="abs" style="left:0;top:0" width="460" height="330"><circle cx="230" cy="175" r="120" fill="none" stroke="#1e9fd6" stroke-width="2" stroke-dasharray="4 5"/></svg>
    <div class="service" style="left:165px;top:0">
      <svg width="26" height="26" viewBox="0 0 26 26"><circle cx="13" cy="13" r="11" fill="none" stroke="#1e9fd6" stroke-width="2"/><ellipse cx="13" cy="13" rx="5" ry="11" fill="none" stroke="#1e9fd6" stroke-width="2"/><line x1="2" y1="13" x2="24" y2="13" stroke="#1e9fd6" stroke-width="2"/></svg>
      INTERNET<br>MEDIA
    </div>
    <div class="service" style="left:60px;top:190px">
      <svg width="26" height="26" viewBox="0 0 26 26"><path d="M3 10h5l10-6v18l-10-6H3z" fill="none" stroke="#1e9fd6" stroke-width="2"/></svg>
      PROMOTION
    </div>
    <div class="service" style="left:275px;top:190px">
      <svg width="26" height="26" viewBox="0 0 26 26"><circle cx="13" cy="8" r="5" fill="none" stroke="#1e9fd6" stroke-width="2"/><path d="M3 24c0-6 4-9 10-9s10 3 10 9" fill="none" stroke="#1e9fd6" stroke-width="2"/></svg>
      INFLUENCER<br>MARKETING
    </div>
  </div>
  <a class="btn-more" style="left:800px;top:396px">MORE ›</a>
</section>

<section class="recruit">
  <div class="recruit-head"><span class="en">RECRUIT</span><span class="ja">KanoMireaの福利厚生や、メンバーの1日の勤務スケジュールを公開</span></div>
  <div class="recruit-card" style="left:220px">
    <p class="card-label">STAFF<br>INTERVIEW</p>
    <div class="card-photo" role="img" aria-label="オフィスで働くスタッフの写真" style="background:linear-gradient(135deg,#e9ecef 0%,#c4cad0 55%,#3f454b 100%)"><span class="card-tag"></span></div>
  </div>
  <div class="recruit-card" style="left:530px">
    <p class="card-label">ONE<br>DAY</p>
    <div class="card-photo" role="img" aria-label="カフェの看板とデスク周りの写真" style="background:linear-gradient(135deg,#b9986d 0%,#e6dccd 50%,#8a7358 100%)"><span class="card-tag"></span></div>
  </div>
  <div class="recruit-card" style="left:840px">
    <p class="card-label">BLOG<br>&nbsp;</p>
    <div class="card-photo" role="img" aria-label="オフィス受付の写真" style="background:linear-gradient(135deg,#5a3d28 0%,#a0784f 45%,#2b2520 100%)"><span class="card-tag"></span></div>
  </div>
</section>

<section class="company">
  <div class="company-head">
    <svg width="22" height="20" viewBox="0 0 22 20"><path d="M2 19V7l9-5 9 5v12z" fill="none" stroke="#333a40" stroke-width="2"/></svg>
    <span class="en">COMPANY</span>
  </div>
  <h2 class="greeting-title">GREETING</h2>
  <p class="greeting-name">代表者 水瀬優斗</p>
  <p class="greeting-text">私たちはインターネットを通じて、人と情報をつなぐ新しい価値を届けてまいります。お客様一人ひとりに寄り添い、信頼される企業を目指し挑戦を続けます。今後とも変わらぬご支援をお願いいたします。</p>
  <a class="btn-more" style="left:620px;top:280px">MORE ›</a>
  <div class="company-thumb" style="left:400px" role="img" aria-label="会議室の写真" style="background:#999">
    <div class="abs" style="inset:0;background:linear-gradient(135deg,#c9ced3,#7d858d)"></div>
    <p class="thumb-label">HISTORY<br>会社沿革</p>
  </div>
  <div class="company-thumb" style="left:610px" role="img" aria-label="社員の集合写真">
    <div class="abs" style="inset:0;background:linear-gradient(135deg,#b8c0c8,#4c545c)"></div>
    <p class="thumb-label">OVERVIEW<br>会社概要</p>
  </div>
  <div class="president-photo" role="img" aria-label="スーツ姿の代表者の写真"></div>
</section>

<footer class="site-footer">
  <div class="footer-nav">
    <div class="footer-col"><h3>COMPANY</h3><p class="sub">会社情報</p><ul><li>代表挨拶</li><li>会社概要</li><li>会社沿革</li></ul></div>
    <div class="footer-col"><h3>BUSINESS</h3><p class="sub">事業内容</p></div>
    <div class="footer-col"><h3>RECRUIT</h3><p class="sub">採用情報</p><ul><li>スタッフインタビュー</li><li>スタッフの1日</li><li>スタッフブログ</li></ul></div>
    <div class="footer-col"><h3>CONTACT</h3><p class="sub">お問い合わせ</p></div>
    <div class="footer-col"><h3>NEWS</h3><p class="sub">新着情報</p></div>
  </div>
  <a class="to-top" aria-label="ページ上部へ"><svg width="16" height="10" viewBox="0 0 16 10"><path d="M1 9l7-7 7 7" fill="none" stroke="#1e9fd6" stroke-width="2"/></svg></a>
  <div class="footer-brand"><span class="brand-dot"></span><span class="brand-name brand-name">Kano Mirea</span></div>
  <p class="footer-address">株式会社 Kano Mirea<br>〒150-0000 東京都渋谷区青葉町1-2-3 青葉ビル5階</p>
</footer>
<div class="copyright">Copyright © 2017 Kano Mirea All Rights Reserved.</div>

</body>
</html>
```